business card/stationary for dental office
Bright Harbor Dental Care
business card/stationary for dental office - Health
Creative Brief
Professional
R. Warren Halvik, DDS
Team Leader
2847 NW 42nd Ave Del City, OK 73115
info@brightharbordentalcare.example
brightharbordentalcare.example
I'll attach and example picture of what i want. text "NO INSURANCE, NO PROBLEM!". "Ask us about our Chairside Savings Plan."
quillmoth quillmoth
pbrandle pbrandle
definately want the back silver not blue

```html
<!DOCTYPE html>
<html lang="en">
<head>
<meta charset="utf-8">
<title>Bright Harbor Dental Care – Business Card</title>
<link rel="stylesheet" href="https://fonts.googleapis.com/css2?family=Raleway:wght@400;500;600;700&display=swap">
<style>
  :root {
    --backdrop: #3a3b3d;
    --card: #fbfbfc;
    --ink: #3c3f44;
    --ink-soft: #55585e;
    --brand-blue: #1e6fcf;
    --icon-grey: #6b6e73;
    --ring-silver: #b9bcc1;
  }
  * { box-sizing: border-box; margin: 0; padding: 0; }
  html, body {
    width: 1200px; height: 816px; overflow: hidden;
    background: var(--backdrop);
    font-family: "Raleway", "Helvetica Neue", Arial, sans-serif;
  }
  .card {
    position: absolute; left: 100px; top: 122px;
    width: 1000px; height: 572px;
    background: var(--card);
    border-radius: 44px;
    color: var(--ink);
  }
  .identity { position: absolute; left: 48px; top: 140px; display: flex; align-items: center; gap: 16px; }
  .identity__avatar { width: 40px; height: 40px; flex: none; }
  .identity__name { font-size: 27px; font-weight: 500; letter-spacing: 1px; text-transform: uppercase; line-height: 1.1; }
  .identity__role { font-size: 21px; font-weight: 400; color: var(--ink-soft); letter-spacing: 0.5px; }
  .divider {
    position: absolute; left: 40px; top: 236px; width: 490px; height: 4px;
    background: var(--brand-blue);
  }
  .contact { position: absolute; left: 52px; display: flex; align-items: center; gap: 22px; }
  .contact__icon { width: 38px; height: 38px; flex: none; }
  .contact__text { font-size: 21px; line-height: 30px; color: var(--ink); letter-spacing: 0.3px; white-space: nowrap; }
  .contact--phone { top: 282px; }
  .contact--web { top: 368px; }
  .contact--address { top: 454px; }
  .brand { position: absolute; left: 580px; top: 238px; display: flex; align-items: center; gap: 18px; }
  .brand__circle { width: 62px; height: 62px; border-radius: 50%; background: var(--ring-silver); flex: none; }
  .brand__name {
    font-size: 36px; font-weight: 600; color: var(--brand-blue);
    line-height: 1.15; letter-spacing: 0.5px;
  }
  .offer { position: absolute; left: 580px; top: 380px; width: 380px; }
  .offer__headline { font-size: 21px; font-weight: 700; color: var(--ink); letter-spacing: 0.5px; }
  .offer__note { font-size: 18px; font-weight: 400; color: var(--ink-soft); margin-top: 6px; line-height: 1.3; }
</style>
</head>
<body>
  <main class="card">
    <div class="identity">
      <svg class="identity__avatar" viewBox="0 0 40 40" aria-hidden="true">
        <circle cx="20" cy="20" r="20" fill="var(--icon-grey)"/>
        <circle cx="20" cy="15" r="6" fill="#fff"/>
        <path d="M9 31c2-7 7-9 11-9s9 2 11 9z" fill="#fff"/>
      </svg>
      <div>
        <p class="identity__name">R. Warren Halvik, DDS</p>
        <p class="identity__role">Team Leader</p>
      </div>
    </div>

    <div class="divider"></div>

    <div class="contact contact--phone">
      <svg class="contact__icon" viewBox="0 0 38 38" aria-hidden="true">
        <circle cx="19" cy="19" r="19" fill="var(--brand-blue)"/>
        <rect x="13" y="9" width="12" height="20" rx="2" fill="none" stroke="#fff" stroke-width="2"/>
        <circle cx="19" cy="25.5" r="1.3" fill="#fff"/>
      </svg>
      <p class="contact__text">(405) 555-0142<br>(405) 555-0187</p>
    </div>

    <div class="contact contact--web">
      <svg class="contact__icon" viewBox="0 0 38 38" aria-hidden="true">
        <circle cx="19" cy="19" r="19" fill="var(--brand-blue)"/>
        <rect x="10" y="11" width="18" height="12" rx="1.5" fill="none" stroke="#fff" stroke-width="2"/>
        <path d="M15 28h8M19 23v5" stroke="#fff" stroke-width="2"/>
      </svg>
      <p class="contact__text">info@brightharbordentalcare.example<br>brightharbordentalcare.example</p>
    </div>

    <div class="contact contact--address">
      <svg class="contact__icon" viewBox="0 0 38 38" aria-hidden="true">
        <circle cx="19" cy="19" r="19" fill="var(--brand-blue)"/>
        <path d="M19 29s-7-7.5-7-12.5a7 7 0 0 1 14 0C26 21.5 19 29 19 29z" fill="#fff"/>
        <circle cx="19" cy="16.5" r="2.6" fill="var(--brand-blue)"/>
      </svg>
      <p class="contact__text">2847 NW 42nd Ave<br>Del City, OK 73115</p>
    </div>

    <div class="brand">
      <span class="brand__circle"></span>
      <p class="brand__name">Bright Harbor<br>Dental Care</p>
    </div>

    <div class="offer">
      <p class="offer__headline">NO INSURANCE, NO PROBLEM!</p>
      <p class="offer__note">Ask us about our Chairside Savings Plan.</p>
    </div>
  </main>
</body>
</html>
```